Business Cards, Letter Heads and a4 size envolpes
Brantwick Holdings
Business Cards, Letter Heads and a4 size envolpes - Financial Services
Creative Brief
Simple
Jad K. Lorenby
Managing Partner
T : +971 4 3867041 M : +971 50 6183024(Ae) M: +255 773 482615 (Tz) P.O. Box 6174 Dubai UAE
jad@brantwickholdings-example.com
www.brantwickholdings-example.com

```html
<!DOCTYPE html>
<html lang="en">
<head>
<meta charset="utf-8">
<title>Brantwick Holdings – Business Card</title>
<link rel="stylesheet" href="https://fonts.googleapis.com/css2?family=Open+Sans:wght@300;400;600&display=swap">
<style>
  :root {
    --page: #e6e6e4;
    --card: #0b0b0b;
    --card-edge: #1c1c1c;
    --ink-light: #f2f2f2;
    --ink-muted: #bdbdbd;
    --icon-bg: #e9e9e9;
    --icon-ink: #111111;
    --tab: #c9c9c9;
    --tab-ink: #3a3a3a;
    --silver-hi: #f4f4f4;
    --silver-lo: #8d8d8d;
  }
  * { box-sizing: border-box; margin: 0; padding: 0; }
  html, body { width: 1200px; height: 900px; overflow: hidden; }
  body {
    background: var(--page);
    font-family: "Open Sans", Arial, sans-serif;
    position: relative;
  }
  .card {
    position: absolute;
    left: 100px; top: 165px;
    width: 1000px; height: 570px;
    background: radial-gradient(ellipse at 50% 30%, var(--card-edge), var(--card) 70%);
    overflow: hidden;
  }
  .brand-name {
    position: absolute;
    top: 200px; left: 0; width: 100%;
    text-align: center;
    font-weight: 300;
    font-size: 44px;
    letter-spacing: 2px;
    color: var(--ink-light);
  }
  .holder {
    position: absolute;
    top: 318px; left: 0; width: 100%;
    padding-left: 70px;
    text-align: center;
    color: var(--ink-light);
    font-size: 17px;
  }
  .holder .person { font-weight: 600; }
  .holder .divider { margin: 0 8px; font-weight: 600; }
  .holder .role { font-weight: 300; font-size: 14px; color: var(--ink-muted); }
  .contacts {
    position: absolute;
    left: 120px; width: 800px;
    display: flex;
    justify-content: space-between;
    color: var(--ink-light);
    font-size: 14px;
    font-weight: 400;
  }
  .contacts.row-one { top: 372px; }
  .contacts.row-two { top: 408px; }
  .contact { display: flex; align-items: center; gap: 7px; white-space: nowrap; }
  .contact svg { width: 18px; height: 18px; flex: none; }
  .silver-rule {
    position: absolute;
    top: 478px; height: 14px;
    background: linear-gradient(180deg, var(--silver-hi), var(--silver-lo) 55%, #5a5a5a);
  }
  .silver-rule.left { left: 0; width: 232px; }
  .silver-rule.right { right: 0; width: 232px; }
  .web-tab {
    position: absolute;
    left: 240px; top: 466px;
    width: 520px; height: 60px;
    background: linear-gradient(180deg, #dadada, var(--tab) 60%, #a9a9a9);
    border-radius: 8px 8px 2px 2px;
    display: flex; align-items: center; justify-content: center;
    color: var(--tab-ink);
    font-size: 19px;
    letter-spacing: 5px;
    font-weight: 400;
  }
</style>
</head>
<body>
  <main class="card">
    <div class="brand-name">Brantwick Holdings</div>

    <div class="holder">
      <span class="person">Jad K. Lorenby</span><span class="divider">|</span><span class="role">Managing Partner</span>
    </div>

    <div class="contacts row-one">
      <span class="contact">
        <svg viewBox="0 0 18 18" aria-hidden="true"><circle cx="9" cy="9" r="9" fill="var(--icon-bg)"/><path d="M4.5 9.2 9 5l4.5 4.2M6 8.4V13h2.2v-2.6h1.6V13H12V8.4" fill="none" stroke="var(--icon-ink)" stroke-width="1.4" stroke-linejoin="round"/></svg>
        P.O. Box 6174 Dubai UAE
      </span>
      <span class="contact">
        <svg viewBox="0 0 18 18" aria-hidden="true"><circle cx="9" cy="9" r="9" fill="var(--icon-bg)"/><path d="M6 4.5c.6-.3 1.1 0 1.4.6l.7 1.4c.2.5 0 .9-.4 1.2l-.5.4c.5 1.2 1.4 2.1 2.6 2.6l.4-.5c.3-.4.7-.6 1.2-.4l1.4.7c.6.3.9.8.6 1.4-.5 1-1.5 1.5-2.6 1.1C8 12.2 5.8 10 5 7.1c-.3-1.1.1-2.1 1-2.6z" fill="var(--icon-ink)"/></svg>
        +971 4 3867041
      </span>
      <span class="contact">
        <svg viewBox="0 0 18 18" aria-hidden="true"><circle cx="9" cy="9" r="9" fill="var(--icon-bg)"/><rect x="6.2" y="4" width="5.6" height="10" rx="1" fill="none" stroke="var(--icon-ink)" stroke-width="1.3"/><circle cx="9" cy="12.2" r=".7" fill="var(--icon-ink)"/></svg>
        +971 50 6183024(Ae)
      </span>
    </div>

    <div class="contacts row-two">
      <span class="contact">
        <svg viewBox="0 0 18 18" aria-hidden="true"><circle cx="9" cy="9" r="9" fill="var(--icon-bg)"/><rect x="6.2" y="4" width="5.6" height="10" rx="1" fill="none" stroke="var(--icon-ink)" stroke-width="1.3"/><circle cx="9" cy="12.2" r=".7" fill="var(--icon-ink)"/></svg>
        +255 773 482615 (Tz)
      </span>
      <span class="contact">
        <svg viewBox="0 0 18 18" aria-hidden="true"><circle cx="9" cy="9" r="9" fill="var(--icon-bg)"/><rect x="4.5" y="5.8" width="9" height="6.4" rx=".6" fill="none" stroke="var(--icon-ink)" stroke-width="1.2"/><path d="M4.8 6.2 9 9.4l4.2-3.2" fill="none" stroke="var(--icon-ink)" stroke-width="1.2"/></svg>
        jad@brantwickholdings-example.com
      </span>
      <span class="contact">
        <svg viewBox="0 0 18 18" aria-hidden="true"><circle cx="9" cy="9" r="9" fill="var(--icon-bg)"/><g fill="none" stroke="var(--icon-ink)" stroke-width="1.1"><circle cx="9" cy="9" r="4.6"/><ellipse cx="9" cy="9" rx="2" ry="4.6"/><path d="M4.4 9h9.2"/></g></svg>
        www.brantwickholdings-example.com
      </span>
    </div>

    <div class="silver-rule left"></div>
    <div class="silver-rule right"></div>
    <div class="web-tab">www.brantwickholdings-example.com</div>
  </main>
</body>
</html>
```